Veltarum

Standard Business Card design.
Sample two-sided design uploaded. White front, Black back.
Would like white shield to be on all black background side.
Willing to look at a couple creative designs, but nothing crazy.
Preference for a classic, confident, strong design.

```html
<!DOCTYPE html>
<html lang="en">
<head>
<meta charset="UTF-8">
<title>Veltarum — Business Card</title>
<link rel="stylesheet" href="https://fonts.googleapis.com/css2?family=Poppins:wght@400;500;600&display=swap">
<style>
  :root {
    --ink: #000000;
    --paper: #ffffff;
    --backdrop: #efefef;
    --text-dark: #111111;
  }
  * { box-sizing: border-box; margin: 0; padding: 0; }
  html, body {
    width: 1200px;
    height: 1200px;
    overflow: hidden;
    background: var(--backdrop);
    font-family: "Poppins", sans-serif;
  }
  .canvas {
    position: relative;
    width: 1200px;
    height: 1200px;
  }
  .card {
    position: absolute;
    left: 150px;
    width: 900px;
    height: 530px;
    overflow: hidden;
  }
  .card--front { top: 52px; background: var(--paper); }
  .card--back { top: 625px; background: var(--ink); }

  .front-panel {
    position: absolute;
    left: 0;
    top: 0;
    width: 900px;
    height: 530px;
  }
  .holder-name {
    position: absolute;
    left: 85px;
    top: 318px;
    color: var(--paper);
    font-weight: 600;
    font-size: 35px;
    line-height: 1.2;
  }
  .wordmark {
    font-family: "Poppins", sans-serif;
    font-weight: 500;
    text-transform: uppercase;
    white-space: nowrap;
  }
  .brand-front {
    position: absolute;
    left: 522px;
    top: 124px;
    display: flex;
    align-items: center;
    gap: 28px;
  }
  .brand-mark--front {
    width: 56px;
    height: 56px;
    border: 5px solid var(--text-dark);
  }
  .wordmark--front {
    font-size: 36px;
    letter-spacing: 4px;
    color: var(--text-dark);
  }
  .contact-list {
    position: absolute;
    right: 60px;
    top: 318px;
    list-style: none;
  }
  .contact-item {
    display: flex;
    align-items: center;
    justify-content: flex-end;
    gap: 16px;
    height: 35px;
    font-size: 21px;
    color: var(--text-dark);
  }
  .contact-icon { width: 16px; height: 16px; flex: none; }

  .brand-mark--back {
    position: absolute;
    left: 222px;
    top: 150px;
    width: 110px;
    height: 110px;
    border: 8px solid var(--paper);
  }
  .wordmark--back {
    position: absolute;
    left: 0;
    width: 554px;
    top: 295px;
    text-align: center;
    font-size: 56px;
    letter-spacing: 8px;
    color: var(--paper);
  }
</style>
</head>
<body>
<main class="canvas">
  <section class="card card--front" aria-label="Card front">
    <svg class="front-panel" viewBox="0 0 900 530" aria-hidden="true">
      <path d="M0 0 H462 V170 C462 330 385 450 237 530 H0 Z" fill="#000"/>
    </svg>
    <p class="holder-name">Mara<br>Ellison</p>
    <div class="brand-front">
      <span class="brand-mark brand-mark--front" aria-hidden="true"></span>
      <p class="wordmark wordmark--front">Veltarum</p>
    </div>
    <ul class="contact-list">
      <li class="contact-item">
        <span>000-410-0000</span>
        <svg class="contact-icon" viewBox="0 0 16 16" aria-hidden="true">
          <path d="M3.5 1.5l2.5 0 1 3.5-1.8 1.2a8 8 0 0 0 4.6 4.6l1.2-1.8 3.5 1v2.5c0 .8-.7 1.5-1.5 1.5A12.5 12.5 0 0 1 2 3c0-.8.7-1.5 1.5-1.5z" fill="#111"/>
        </svg>
      </li>
      <li class="contact-item">
        <span>mara@veltarum.com</span>
        <svg class="contact-icon" viewBox="0 0 16 16" aria-hidden="true">
          <rect x="1" y="3" width="14" height="10" fill="#111"/>
          <path d="M1.5 3.5L8 9l6.5-5.5" fill="none" stroke="#fff" stroke-width="1.2"/>
        </svg>
      </li>
      <li class="contact-item">
        <span>www.veltarum.com</span>
        <svg class="contact-icon" viewBox="0 0 16 16" aria-hidden="true">
          <circle cx="8" cy="8" r="6.5" fill="none" stroke="#111" stroke-width="1.5"/>
          <ellipse cx="8" cy="8" rx="2.6" ry="6.5" fill="none" stroke="#111" stroke-width="1.2"/>
          <line x1="1.5" y1="8" x2="14.5" y2="8" stroke="#111" stroke-width="1.2"/>
        </svg>
      </li>
    </ul>
  </section>

  <section class="card card--back" aria-label="Card back">
    <span class="brand-mark brand-mark--back" aria-hidden="true"></span>
    <p class="wordmark wordmark--back">Veltarum</p>
  </section>
</main>
</body>
</html>
```